hello! I need a very simple modern business card for a new venture called The Quiet Harbour Asia. It's the very first Tech-Free retreat in Asia!

The concept is very unique. Basically a group of 12-15 people would go on a 3 to 4 days retreat where no phone or internet is allowed. The first retreat will take place in a beautiful villa in Bali by the sea. It will include yoga, meditation, art & writing workshops, swimming, hiking, cooking, healthy vegetarian meals, etc.

Reason: Thanks for your submissions. I still haven't found exactly what I'm after but the designs that haven't be eliminated are getting close.. Please keep in mind that it should be a simple, modern and upmarket business card. Thanks

Target Market(s)

Both men and women who would like to disconnect from life, computer and phone for 3/4 days. They can be either local or expats but based in Asia (Singapore, Hong Kong).
Client will have to pay for their own flight and then the price is around US$600 for a 3-day retreat including everything (accommodation, food, activities). It means clients already have a good income. They are usually working in marketing, advertising, digital media, public relations.

Industry/Entity Type

Internet

Font styles to use
Other font styles liked:
• anything modern you like

Colors
acd036
9bcb3c
f37022
f68d4d
1b1b1b
333333
acd037

Requirements
Must have
• Name: Rel Vontaine
Position: #screenwanderer
Company: The Quiet Harbour Asia (asia should be smaller than the rest)
- Email button - quietharbourasia@mailnest.example
- Facepage button - www.facepage.example/quietharbourasia
- Ticketloom button - www.quietharbourasia.ticketloom.example
Nice to have
• You can use my logo attached but it's something I designed quickly on Power Point so it would be nice to include your own version.
Should not have
• anything tacky or girly or childish. thanks

```html
<!DOCTYPE html>
<html lang="en">
<head>
<meta charset="utf-8">
<title>The Quiet Harbour Asia – Business Card</title>
<link href="https://fonts.googleapis.com/css2?family=Tenor+Sans&display=swap" rel="stylesheet">
<style>
  :root {
    --backdrop: #ece8e3;
    --card: #ffffff;
    --leaf-green: #acd036;
    --ink: #1b1b1b;
    --ink-soft: #333333;
    --orange: #f68d4d;
    --orange-deep: #f37022;
    --social-blue: #3b5a98;
  }
  * { box-sizing: border-box; margin: 0; padding: 0; }
  html, body {
    width: 1200px; height: 1000px; overflow: hidden;
    background: var(--backdrop);
    font-family: "Tenor Sans", sans-serif;
    color: var(--ink);
  }
  .canvas { position: relative; width: 1200px; height: 1000px; }

  .card {
    position: absolute;
    width: 540px; height: 310px;
    background: var(--card);
    box-shadow: 0 6px 18px rgba(0,0,0,0.18);
  }
  .card--front { left: 150px; top: 170px; border-right: 2px solid var(--leaf-green); }
  .card--back { left: 510px; top: 520px; }

  .rule {
    position: absolute; height: 2px; background: var(--leaf-green);
  }

  /* front */
  .holder {
    position: absolute; right: 40px; top: 34px; text-align: right;
  }
  .holder__name { font-size: 30px; color: var(--ink); letter-spacing: 0.5px; line-height: 1.1; }
  .holder__title { font-size: 19px; color: var(--orange); line-height: 1.2; }
  .card--front .rule { left: 30px; right: 0; top: 118px; }

  .brand {
    position: absolute; display: flex; align-items: center; gap: 10px;
  }
  .brand__dot {
    width: 16px; height: 16px; border-radius: 50%; background: var(--leaf-green);
  }
  .brand__name { font-size: 18px; color: var(--ink); }
  .card--front .brand { left: 60px; top: 86px; }

  .contacts {
    position: absolute; right: 40px; top: 138px; list-style: none;
  }
  .contacts li {
    display: flex; justify-content: flex-end; align-items: center; gap: 12px;
    font-size: 15px; color: var(--ink-soft); height: 30px;
  }
  .icon { width: 22px; height: 22px; border-radius: 3px; flex: none; }
  .icon--mail { background: var(--leaf-green); }
  .icon--facepage { background: var(--social-blue); }
  .icon--ticketloom { background: var(--orange-deep); }

  /* back */
  .card--back .rule--short { left: 14px; width: 70px; top: 162px; }
  .card--back .rule--long { left: 130px; right: 40px; top: 186px; }
  .card--back .brand { left: 110px; top: 148px; }
  .card--back .brand__name { font-size: 21px; }
</style>
</head>
<body>
<main class="canvas">
  <section class="card card--front" aria-label="Card front">
    <div class="holder">
      <p class="holder__name">Rel Vontaine</p>
      <p class="holder__title">#screenwanderer</p>
    </div>
    <div class="brand">
      <span class="brand__dot"></span>
      <span class="brand__name">The Quiet Harbour Asia</span>
    </div>
    <div class="rule"></div>
    <ul class="contacts">
      <li>quietharbourasia@mailnest.example
        <svg class="icon icon--mail" viewBox="0 0 22 22" aria-hidden="true">
          <rect width="22" height="22" rx="3" fill="#acd036"/>
          <rect x="4" y="6" width="14" height="10" fill="none" stroke="#fff" stroke-width="1.5"/>
          <polyline points="4,6 11,12 18,6" fill="none" stroke="#fff" stroke-width="1.5"/>
        </svg>
      </li>
      <li>www.facepage.example/quietharbourasia <span class="icon icon--facepage"></span></li>
      <li>www.quietharbourasia.ticketloom.example <span class="icon icon--ticketloom"></span></li>
    </ul>
  </section>

  <section class="card card--back" aria-label="Card back">
    <div class="rule rule--short"></div>
    <div class="brand">
      <span class="brand__dot"></span>
      <span class="brand__name">The Quiet Harbour Asia</span>
    </div>
    <div class="rule rule--long"></div>
  </section>
</main>
</body>
</html>
```